Label Design for Food Brand

We want a modern label for our spice blends. We are completely open in which direction, it should be modern and beautiful.

Use for Sample spice mixture: "BBQ Tanqo"

Here the Packaging:
https://www.orv-plimkevar.com/media/xlarge/1700_1.jpg
Abmessung: Ø 54 x 67 mm

Target Market(s)

Food

Industry/Entity Type

Food

Requirements
Must have
• Logo, Name of Tanqo
Should not have
• Images of food

```html
<!DOCTYPE html>
<html lang="en">
<head>
<meta charset="utf-8">
<title>Tanqo Food – BBQ Tanqo Spice Mixture Label</title>
<link rel="stylesheet" href="https://fonts.googleapis.com/css2?family=Bebas+Neue&family=Montserrat:wght@600&display=swap">
<style>
  :root {
    --page: #ffffff;
    --wood-light: #ece5e1;
    --wood-light-edge: #e2d9d4;
    --label-red: #a30a0c;
    --label-red-deep: #8f0608;
    --ornament-tone: #b0211f;
    --ink-white: #ffffff;
  }
  * { margin: 0; padding: 0; box-sizing: border-box; }
  html, body { width: 1200px; height: 915px; overflow: hidden; background: var(--page); }
  .canvas { position: relative; width: 1200px; height: 915px; }

  .wood-board {
    position: absolute; left: 222px; top: 153px; width: 742px; height: 598px;
    background: linear-gradient(180deg, var(--wood-light) 0%, var(--wood-light-edge) 50%, var(--wood-light) 100%);
  }
  .label-shape { position: absolute; left: 0; top: 0; width: 1200px; height: 915px; }

  .star-row {
    position: absolute; left: 412px; top: 238px; width: 360px; height: 82px;
    background: var(--ornament-tone); border-radius: 6px;
  }

  .brand-name {
    position: absolute; left: 269px; width: 656px; top: 340px;
    text-align: center; color: var(--ink-white);
    font-family: "Montserrat", sans-serif; font-weight: 600;
    font-size: 74px; line-height: 1; letter-spacing: 1px;
  }

  .rule { position: absolute; left: 320px; width: 546px; height: 4px; background: var(--ink-white); }
  .rule--top { top: 455px; }
  .rule--bottom { top: 608px; }

  .product-name {
    position: absolute; left: 269px; width: 656px; top: 466px;
    text-align: center; color: var(--ink-white);
    font-family: "Bebas Neue", sans-serif; font-size: 148px; line-height: 1;
    letter-spacing: 4px;
  }

  .product-type {
    position: absolute; left: 453px; top: 612px; width: 281px; height: 53px;
    background: var(--ink-white); border-radius: 0 0 8px 8px;
    display: flex; align-items: center; justify-content: center;
    color: var(--label-red);
    font-family: "Bebas Neue", sans-serif; font-size: 50px; line-height: 1;
    letter-spacing: 1px; padding-top: 4px;
  }
</style>
</head>
<body>
  <main class="canvas">
    <div class="wood-board" role="img" aria-label="Light whitewashed wood plank background"></div>

    <svg class="label-shape" viewBox="0 0 1200 915" aria-hidden="true">
      <defs>
        <linearGradient id="labelRed" x1="0" y1="0" x2="0" y2="1">
          <stop offset="0" stop-color="var(--label-red)"/>
          <stop offset="0.5" stop-color="var(--label-red-deep)"/>
          <stop offset="1" stop-color="var(--label-red)"/>
        </linearGradient>
      </defs>
      <path class="label-panel" fill="url(#labelRed)"
        d="M313 192 H881 A44 44 0 0 0 925 236 V668 A44 44 0 0 0 881 712 H313 A44 44 0 0 0 269 668 V236 A44 44 0 0 0 313 192 Z"/>
      <path class="label-frame" fill="none" stroke="#ffffff" stroke-width="3"
        d="M321 203 H873 A40 40 0 0 0 914 244 V660 A40 40 0 0 0 873 701 H321 A40 40 0 0 0 280 660 V244 A40 40 0 0 0 321 203 Z"/>
    </svg>

    <div class="star-row" role="img" aria-label="Row of five stars above the brand name"></div>

    <div class="brand-name">TANQOFOOD</div>

    <div class="rule rule--top"></div>
    <h1 class="product-name">BBQ TANQO</h1>
    <div class="rule rule--bottom"></div>

    <div class="product-type">SPICE MIXTURE</div>
  </main>
</body>
</html>
```